Process Graphic for website

We would like to design a graphic that shows our internal process for scanning our customer records. Our process is listed in order below:
Transport Documents
Inventory Records
Document Preparation
Scan Documents
AI & Data Extraction
Quality Control
Deliver Documents
Records Retention or Destruction

Our customers need to know that we have a clear defined process for scanning records and it needs to visually demonstrate that in a simple way. I have attached our logo as these are the colors of our new website so whatever colors you chose should match our site.

```html
<!DOCTYPE html>
<html lang="en">
<head>
<meta charset="utf-8">
<title>Internal Process for Scanning Our Customer Records</title>
<link href="https://fonts.googleapis.com/css2?family=Michroma&family=Saira+Condensed:wght@600&family=Archivo:wght@800&display=swap" rel="stylesheet">
<style>
  :root {
    --navy: #24248f;
    --gold: #c9930f;
    --lavender: #d6d6f2;
    --paper: #ffffff;
    --backdrop: #e6e6e8;
  }
  html, body { margin: 0; padding: 0; overflow: hidden; }
  body { width: 836px; height: 1200px; background: var(--backdrop); position: relative; }
  .process-graphic { position: absolute; left: 0; top: 303px; width: 836px; height: 593px; background: var(--paper); }
  .process-graphic svg { display: block; }
  .title-small, .title-large, .banner-text { font-family: "Michroma", sans-serif; }
  .title-small { fill: var(--navy); stroke: var(--navy); stroke-width: 0.5; font-size: 17px; }
  .title-large { fill: var(--gold); stroke: var(--gold); stroke-width: 0.8; font-size: 27px; }
  .banner { fill: var(--navy); }
  .banner-text { fill: #fff; stroke: #fff; stroke-width: 0.8; font-size: 30px; }
  .timeline-line { stroke: var(--lavender); stroke-width: 4; }
  .step-halo { fill: none; stroke: var(--lavender); stroke-width: 4; }
  .step-pill { fill: var(--paper); stroke: var(--navy); stroke-width: 1.4; }
  .step-divider { stroke: var(--navy); stroke-width: 1.2; }
  .step-label { font-family: "Saira Condensed", sans-serif; font-weight: 600; font-size: 16.5px; fill: var(--navy); text-anchor: middle; }
  .step-number { font-family: "Archivo", sans-serif; font-weight: 800; font-size: 46px; fill: var(--gold); text-anchor: middle; }
  .step-chevron { fill: none; stroke: var(--navy); stroke-width: 1.6; }
  .icon-disc { fill: var(--gold); }
  .icon-line { fill: none; stroke: #fff; stroke-width: 2; stroke-linecap: round; stroke-linejoin: round; }
  .brand-name { font-family: "Archivo", sans-serif; font-weight: 800; font-size: 38px; fill: var(--navy); text-anchor: middle; }
  .brand-mark { fill: var(--navy); }
</style>
</head>
<body>
<main class="process-graphic">
<svg width="836" height="593" viewBox="0 0 836 593" xmlns="http://www.w3.org/2000/svg">
  <defs>
    <g id="chevron-down" class="step-chevron"><path d="M-9 0 L0 6 L9 0"/><path d="M-9 5 L0 11 L9 5"/></g>
    <g id="chevron-up" class="step-chevron"><path d="M-9 11 L0 5 L9 11"/><path d="M-9 6 L0 0 L9 6"/></g>
    <path id="pill-top" class="step-pill" d="M0 323 L0 213 Q0 193 20 193 L75 193 Q95 193 95 213 L95 323 A47.5 47.5 0 0 1 0 323 Z"/>
    <path id="pill-bottom" class="step-pill" d="M0 323 A47.5 47.5 0 0 1 95 323 L95 432 Q95 452 75 452 L20 452 Q0 452 0 432 Z"/>
    <circle id="halo" class="step-halo" cx="47.5" cy="323" r="49.5"/>
    <circle id="disc" class="icon-disc" cx="47.5" cy="323" r="43"/>
  </defs>

  <!-- heading -->
  <text class="title-small" x="21" y="74" textLength="306" lengthAdjust="spacingAndGlyphs">INTERNAL PROCESS FOR</text>
  <text class="title-large" x="19" y="108" textLength="309" lengthAdjust="spacingAndGlyphs">SCANNING OUR</text>
  <polygon class="banner" points="352,59 812,59 802,109 342,109"/>
  <text class="banner-text" x="362" y="99" textLength="430" lengthAdjust="spacingAndGlyphs">CUSTOMER RECORDS</text>

  <!-- timeline -->
  <line class="timeline-line" x1="0" y1="323" x2="836" y2="323"/>

  <!-- 1 Transport -->
  <g class="step step-top" transform="translate(12 0)">
    <use href="#halo"/><use href="#pill-top"/>
    <line class="step-divider" x1="0" y1="246" x2="95" y2="246"/>
    <text class="step-label" x="47.5" y="219">Transport</text>
    <text class="step-label" x="47.5" y="237">Documents</text>
    <use href="#disc"/>
    <g class="icon-line" aria-label="Truck carrying documents icon" role="img">
      <rect x="23" y="305" width="20" height="26"/><path d="M27 312h12M27 318h12M27 324h8"/>
      <path d="M43 316h14l8 9v9H23v-3"/><circle cx="31" cy="336" r="3.5"/><circle cx="57" cy="336" r="3.5"/>
    </g>
    <use href="#chevron-up" x="47.5" y="396"/>
    <text class="step-number" x="47.5" y="447">1</text>
  </g>
  <!-- 3 Preparation -->
  <g class="step step-top" transform="translate(216 0)">
    <use href="#halo"/><use href="#pill-top"/>
    <line class="step-divider" x1="0" y1="246" x2="95" y2="246"/>
    <text class="step-label" x="47.5" y="219">Document</text>
    <text class="step-label" x="47.5" y="237">Preparation</text>
    <use href="#disc"/>
    <g class="icon-line" aria-label="Checklist clipboard icon" role="img">
      <rect x="30" y="303" width="35" height="42" rx="4"/><rect x="40" y="299" width="15" height="7" rx="2"/>
      <path d="M35 316l2 2 4-4M45 316h14M35 326l2 2 4-4M45 326h14M35 336l2 2 4-4M45 336h14"/>
    </g>
    <use href="#chevron-up" x="47.5" y="396"/>
    <text class="step-number" x="47.5" y="447">3</text>
  </g>
  <!-- 5 AI -->
  <g class="step step-top" transform="translate(421 0)">
    <use href="#halo"/><use href="#pill-top"/>
    <line class="step-divider" x1="0" y1="246" x2="95" y2="246"/>
    <text class="step-label" x="47.5" y="219">AI &amp; Data</text>
    <text class="step-label" x="47.5" y="237">Extraction</text>
    <use href="#disc"/>
    <g class="icon-line" aria-label="Processor chip icon" role="img">
      <rect x="34" y="309" width="27" height="27" rx="2"/><rect x="41" y="316" width="13" height="13"/>
      <path d="M40 309v-6M47.5 309v-6M55 309v-6M40 336v6M47.5 336v6M55 336v6M34 315h-6M34 322.5h-6M34 330h-6M61 315h6M61 322.5h6M61 330h6"/>
    </g>
    <use href="#chevron-up" x="47.5" y="396"/>
    <text class="step-number" x="47.5" y="447">5</text>
  </g>
  <!-- 7 Deliver -->
  <g class="step step-top" transform="translate(625 0)">
    <use href="#halo"/><use href="#pill-top"/>
    <line class="step-divider" x1="0" y1="246" x2="95" y2="246"/>
    <text class="step-label" x="47.5" y="219">Deliver</text>
    <text class="step-label" x="47.5" y="237">Documents</text>
    <use href="#disc"/>
    <g class="icon-line" aria-label="Delivered document icon" role="img">
      <rect x="33" y="301" width="30" height="38" rx="2"/><path d="M38 309h12M38 316h20M38 323h10"/>
      <rect x="50" y="326" width="11" height="10"/><path d="M52 331l2 2 5-5M25 333h10l6 6h-16"/>
    </g>
    <use href="#chevron-up" x="47.5" y="396"/>
    <text class="step-number" x="47.5" y="447">7</text>
  </g>

  <!-- 2 Inventory -->
  <g class="step step-bottom" transform="translate(113 0)">
    <text class="step-number" x="47.5" y="232">2</text>
    <use href="#chevron-down" x="47.5" y="249"/>
    <use href="#halo"/><use href="#pill-bottom"/>
    <line class="step-divider" x1="0" y1="398" x2="95" y2="398"/>
    <use href="#disc"/>
    <g class="icon-line" aria-label="Inventory list icon" role="img">
      <rect x="28" y="301" width="34" height="44" rx="3"/>
      <circle cx="38" cy="311" r="4"/><circle cx="50" cy="313" r="3"/>
      <path d="M33 324l2 2 3-3M42 325h14M33 333l2 2 3-3M42 334h14M66 312l-8 26-2 5"/>
    </g>
    <text class="step-label" x="47.5" y="420">Inventory</text>
    <text class="step-label" x="47.5" y="438">Records</text>
  </g>
  <!-- 4 Scan -->
  <g class="step step-bottom" transform="translate(318 0)">
    <text class="step-number" x="47.5" y="232">4</text>
    <use href="#chevron-down" x="47.5" y="249"/>
    <use href="#halo"/><use href="#pill-bottom"/>
    <line class="step-divider" x1="0" y1="398" x2="95" y2="398"/>
    <use href="#disc"/>
    <g class="icon-line" aria-label="Document scan icon" role="img">
      <path d="M25 309v-8h8M62 301h8v8M70 337v8h-8M33 345h-8v-8"/>
      <path d="M38 306h13l6 6v26H38Z"/><path d="M30 323h35M42 331h11"/>
    </g>
    <text class="step-label" x="47.5" y="420">Scan</text>
    <text class="step-label" x="47.5" y="438">Documents</text>
  </g>
  <!-- 6 Quality -->
  <g class="step step-bottom" transform="translate(522 0)">
    <text class="step-number" x="47.5" y="232">6</text>
    <use href="#chevron-down" x="47.5" y="249"/>
    <use href="#halo"/><use href="#pill-bottom"/>
    <line class="step-divider" x1="0" y1="398" x2="95" y2="398"/>
    <use href="#disc"/>
    <g class="icon-line" aria-label="Quality check tick icon" role="img">
      <circle cx="47.5" cy="323" r="20" stroke-dasharray="6 3"/><circle cx="47.5" cy="323" r="13"/>
      <path d="M41 323l5 5 9-9"/>
    </g>
    <text class="step-label" x="47.5" y="420">Quality</text>
    <text class="step-label" x="47.5" y="438">Control</text>
  </g>
  <!-- 8 Retention -->
  <g class="step step-bottom" transform="translate(726 0)">
    <text class="step-number" x="47.5" y="232">8</text>
    <use href="#chevron-down" x="47.5" y="249"/>
    <use href="#halo"/><use href="#pill-bottom"/>
    <line class="step-divider" x1="0" y1="380" x2="95" y2="380"/>
    <use href="#disc"/>
    <g class="icon-line" aria-label="Document shredder icon" role="img">
      <path d="M38 314v-14h14l5 5v9"/><path d="M42 306h8"/>
      <rect x="27" y="314" width="41" height="15" rx="2"/>
      <path d="M33 333v3M38 333v6M43 333v4M48 333v7M53 333v4M58 333v6M63 333v3"/>
    </g>
    <text class="step-label" x="47.5" y="402">Records</text>
    <text class="step-label" x="47.5" y="420">Retention or</text>
    <text class="step-label" x="47.5" y="438">Destruction</text>
  </g>

  <!-- brand -->
  <rect class="brand-mark" x="234" y="524" width="12" height="12"/>
  <text class="brand-name" x="432" y="545">Lumora Records Co</text>
</svg>
</main>
</body>
</html>
```